Website Design for new business Junior Stride Athletics

We need a website for our new business Junior Stride Athletics which is about teaching kids from 5 years to 16 years of age how to play either Australian Rules Football or Soccer. Need area for Soccer and Football plus Coaches section, and schedule for each training etc. NEW LOGO ADDED

Target Market(s)

Adults with kids from 5 to 16 looking for specialist coaches to train their kids

Industry/Entity Type

Fitness

Number of Pages Required

5+ page

Colors
3176b5
ffc214

Requirements
Must have
• Logo
• How, Why and What
Nice to have
• I like this website http://www.bramblewickgames.com.au/
• http://www.quillhavenplaydrills.com.au/ is another site that is okay
Should not have
• Our competitor is this website http://www.marrowvaleyouthclinic.com.au/ but I don't like their website style not kid or parent friendly

```html
<!DOCTYPE html>
<html lang="en">
<head>
<meta charset="utf-8">
<title>Junior Stride Athletics – Where Kids Are Champions</title>
<link href="https://fonts.googleapis.com/css2?family=Oswald:wght@400;500;700&family=Open+Sans:wght@400;600;700&display=swap" rel="stylesheet">
<style>
:root{
  --blue:#3176b5;
  --blue-dark:#245a8c;
  --yellow:#ffc214;
  --navy:#0f2440;
  --ink:#1d2229;
  --text:#4a4f55;
  --grey:#eceeef;
  --red:#c8322b;
  --white:#ffffff;
}
*{box-sizing:border-box;margin:0;padding:0}
html,body{width:1200px;height:3260px;overflow:hidden}
body{font-family:"Open Sans",Arial,sans-serif;color:var(--text);background:var(--white);position:relative}
.section{position:absolute;left:0;width:1200px;overflow:hidden}
.heading{font-family:"Oswald","Arial Narrow",sans-serif;font-weight:700;text-transform:uppercase}
.photo{position:absolute}
.marker{position:absolute;left:588px;width:0;height:0;border-left:12px solid transparent;border-right:12px solid transparent;border-top:12px solid var(--red);z-index:5}

/* header */
.site-header{top:0;height:120px;background:var(--white)}
.brand{position:absolute;left:120px;top:30px;display:flex;align-items:center;gap:14px}
.brand-dot{width:52px;height:52px;border-radius:50%;background:var(--blue)}
.brand-name{font-family:"Oswald",sans-serif;font-weight:700;font-size:26px;color:var(--navy);text-transform:uppercase}
.contact-phone{position:absolute;right:120px;top:26px;display:flex;align-items:center;gap:8px;font-size:16px;color:var(--ink);font-weight:600}
.tagline{position:absolute;right:120px;top:66px;font-family:"Oswald",sans-serif;font-weight:700;font-size:26px;color:var(--navy)}

/* hero */
.hero{top:120px;height:500px}
.hero-photo{left:0;top:0;width:1200px;height:500px;background:linear-gradient(180deg,#7c8f8a 0%,#5d7a63 35%,#4f8b3c 60%,#3f7a2c 100%)}
.hero-copy{position:absolute;left:640px;top:140px;width:520px;text-align:center;color:var(--white)}
.hero-title{font-family:"Open Sans",sans-serif;font-weight:700;font-size:26px;line-height:1.3}
.hero-sub{font-size:15px;margin-top:10px;font-weight:600}
.btn-yellow{display:inline-block;background:var(--yellow);color:var(--navy);font-family:"Oswald",sans-serif;font-weight:500;font-size:15px;padding:8px 22px;border-radius:3px;text-transform:uppercase;margin-top:18px}
.hero-dots{position:absolute;left:1040px;top:368px;display:flex;gap:8px}
.hero-dots span{width:10px;height:10px;border-radius:50%;background:rgba(255,255,255,.6)}
.hero-dots span:first-child{background:var(--white)}

/* approach cards */
.approach{top:620px;height:440px;background:var(--grey)}
.approach-card{position:absolute;top:56px;width:270px;height:340px;background:var(--white);border:1px solid #d7dadd;box-shadow:0 2px 6px rgba(0,0,0,.12);text-align:center;padding:8px}
.approach-card .photo{position:relative;width:252px;height:130px;background:linear-gradient(180deg,#9fb6c6,#5c8a4a)}
.approach-card h3{font-family:"Oswald",sans-serif;font-weight:700;font-size:22px;color:var(--navy);margin-top:16px}
.approach-card p{font-size:12px;line-height:1.55;margin:8px 12px 0}
.btn-small{display:inline-block;background:var(--blue);color:var(--white);font-size:11px;font-weight:700;padding:5px 14px;margin-top:12px;text-transform:uppercase}
.slide-arrow{position:absolute;top:210px;width:0;height:0;border-top:12px solid transparent;border-bottom:12px solid transparent}
.slide-arrow.prev{left:120px;border-right:14px solid #fff}
.slide-arrow.next{left:1066px;border-left:14px solid #fff}

/* coaches */
.coaches{top:1060px;height:540px;background:radial-gradient(ellipse at 50% 30%,#2d5a8a 0%,#173659 55%,#0b1c33 100%);color:#dbe4ee}
.coaches-title{position:absolute;top:90px;width:1200px;text-align:center;font-family:"Oswald",sans-serif;font-weight:700;font-size:34px;color:var(--white)}
.coaches-title .accent{color:var(--yellow)}
.coaches-sub{position:absolute;top:148px;width:1200px;text-align:center;font-size:14px;font-weight:600;color:var(--white)}
.coach-photo{left:165px;top:200px;width:255px;height:220px;border:5px solid var(--white);background:linear-gradient(180deg,#7aa0c0,#4f8f3a)}
.coach-bio{position:absolute;left:450px;top:200px;width:600px}
.coach-bio h3{font-family:"Open Sans",sans-serif;font-weight:700;font-size:22px;color:var(--white)}
.coach-bio p{font-size:13px;line-height:1.7;margin-top:12px}

/* clinics */
.clinics{top:1600px;height:400px;background:var(--white)}
.clinics h2{position:absolute;left:160px;top:40px;font-size:34px;color:var(--ink)}
.clinics-copy{position:absolute;left:160px;top:100px;width:560px;font-size:13px;line-height:1.7}
.clinic-details{list-style:none;margin-top:14px;font-weight:700;color:var(--ink);font-size:12px;line-height:1.8}
.clinic-photo{left:760px;top:80px;width:280px;height:270px;border:4px solid var(--blue);background:linear-gradient(180deg,#8fb0c4,#4c8a3e)}

/* special offer */
.offer{top:2000px;height:420px;background:radial-gradient(ellipse at 70% 50%,#3b4550 0%,#1a1f26 60%,#0e1116 100%);color:#cfd4da}
.offer-photo{left:170px;top:100px;width:250px;height:190px;border:5px solid var(--white);background:linear-gradient(180deg,#9cb8d0,#4d8a3c)}
.offer-copy{position:absolute;left:470px;top:100px;width:590px}
.offer-copy h2{font-size:36px;color:var(--yellow)}
.offer-copy .offer-sub{font-size:14px;font-weight:600;color:var(--white);margin-top:2px}
.offer-copy p{font-size:13px;line-height:1.7;margin-top:14px}

/* pricing */
.pricing{top:2420px;height:200px;background:var(--grey)}
.price-box{position:absolute;top:45px;width:420px;height:110px;display:flex;align-items:center;padding-left:26px;gap:24px;color:var(--white)}
.price-box.past{left:160px;background:#2a3036}
.price-box.new{left:620px;background:var(--blue)}
.price-badge{width:72px;height:72px;border-radius:50%;border:3px solid var(--yellow);display:flex;align-items:center;justify-content:center;font-family:"Oswald",sans-serif;font-weight:700;font-size:22px}
.price-label .heading{font-size:30px;font-weight:500;line-height:1.1}
.price-label .who{font-size:14px;font-weight:700;text-transform:uppercase;color:var(--yellow)}
.price-box.new .who{color:var(--white)}

/* call to action */
.cta{top:2620px;height:180px;text-align:center}
.cta h2{margin-top:36px;font-size:40px;color:var(--blue)}
.cta p{font-family:"Oswald",sans-serif;font-size:28px;color:var(--ink);margin-top:4px}

/* register */
.register{top:2800px;height:370px;background:linear-gradient(180deg,#22303d,#101820)}
.register-form{position:absolute;left:160px;top:80px;width:300px}
.field{height:34px;background:var(--white);margin-bottom:14px;font-size:13px;color:#888;padding:8px 12px}
.field-label{font-size:12px;color:var(--white);margin-bottom:4px}
.btn-send{display:inline-block;background:var(--blue);color:var(--white);font-size:13px;font-weight:700;padding:7px 22px;text-transform:uppercase}
.register-photo{left:620px;top:40px;width:420px;height:330px;background:linear-gradient(180deg,#a0b4c2 0%,#8a9aa6 45%,#4f8c3e 100%)}

/* footer */
.site-footer{top:3170px;height:90px;background:var(--blue);color:var(--white);font-size:12px}
.footer-email{position:absolute;left:160px;top:24px;display:flex;align-items:center;gap:8px}
.footer-legal{position:absolute;left:160px;top:54px;opacity:.85}
.follow{position:absolute;right:160px;top:20px;text-align:right}
.socials{display:flex;gap:8px;margin-top:8px;justify-content:flex-end}
.socials span{width:24px;height:24px;border-radius:50%;background:var(--white)}
</style>
</head>
<body>

<header class="section site-header">
  <div class="brand"><span class="brand-dot"></span><span class="brand-name">Junior Stride Athletics</span></div>
  <div class="contact-phone">
    <svg width="16" height="16" viewBox="0 0 24 24"><path fill="#3176b5" d="M6.6 10.8a15 15 0 006.6 6.6l2.2-2.2a1 1 0 011-.25 11.4 11.4 0 003.6.57 1 1 0 011 1V20a1 1 0 01-1 1A17 17 0 013 4a1 1 0 011-1h3.5a1 1 0 011 1c0 1.25.2 2.45.57 3.6a1 1 0 01-.25 1z"/></svg>
    03 9555 0142
  </div>
  <div class="tagline heading">Where Kids Are Champions</div>
</header>

<section class="section hero">
  <div class="photo hero-photo" role="img" aria-label="Children in team shirts playing soccer on a grass field"></div>
  <div class="hero-copy">
    <h1 class="hero-title">Specialist Sports Coaching<br>For Boys &amp; Girls 5 To 16 Years Old</h1>
    <p class="hero-sub">Is Your Child The Next Champion? Click Here For Details</p>
    <span class="btn-yellow">Take Here Free Trial &rsaquo;</span>
  </div>
  <div class="hero-dots"><span></span><span></span><span></span></div>
</section>
<div class="marker" style="top:620px"></div>

<section class="section approach">
  <span class="slide-arrow prev"></span>
  <article class="approach-card" style="left:160px">
    <div class="photo" role="img" aria-label="Close view of young players kicking a soccer ball"></div>
    <h3>WHY WE DO IT</h3>
    <p>We love seeing kids step away from screens and into fresh air, building skills, friendships and confidence through every game.</p>
    <span class="btn-small">Learn More</span>
  </article>
  <article class="approach-card" style="left:465px">
    <div class="photo" role="img" aria-label="Junior team training together on the field"></div>
    <h3>HOW WE DO IT</h3>
    <p>Small groups, qualified coaches and fun drills mean every child gets time on the ball and clear guidance each week.</p>
    <span class="btn-small">Learn More</span>
  </article>
  <article class="approach-card" style="left:770px">
    <div class="photo" role="img" aria-label="Coach with a group of kids in blue training tops"></div>
    <h3>WHAT WE DO</h3>
    <p>We run soccer and Australian Rules clinics for boys and girls aged five to sixteen, from first kicks to match play.</p>
    <span class="btn-small">Learn More</span>
  </article>
  <span class="slide-arrow next"></span>
</section>
<div class="marker" style="top:1060px"></div>

<section class="section coaches">
  <h2 class="coaches-title"><span class="accent">Coaches</span> &amp; Australian Rules</h2>
  <p class="coaches-sub">There are 3 principles we bring to every session we run</p>
  <div class="photo coach-photo" role="img" aria-label="Coach running a junior football session"></div>
  <div class="coach-bio">
    <h3>About Daniel Moreton</h3>
    <p>Daniel brings over fifteen years of coaching to every session, with a calm and encouraging style that helps young players feel welcome, supported and ready to try something new on the field.</p>
    <p>He has coached junior squads across local clubs and regional programs, focusing on fundamentals, teamwork and fair play while keeping every drill fun, active and suited to each age group.</p>
    <p>Our sessions are planned so every child gets plenty of touches of the ball, clear feedback and a real sense of progress from week to week.</p>
  </div>
</section>
<div class="marker" style="top:1600px"></div>

<section class="section clinics">
  <h2 class="heading">Weekly Clinics</h2>
  <div class="clinics-copy">
    <p>Our weekly clinics run through the term and cover kicking, passing, marking, dribbling and game sense. Groups are sorted by age and skill so every child is challenged at the right level. Sessions are led by qualified coaches in a safe and friendly setting, and parents are always welcome to watch from the sideline and cheer on their young champions.</p>
    <ul class="clinic-details">
      <li>DURATION : 1 HOUR SESSIONS</li>
      <li>VENUE : PARKSIDE OVAL</li>
      <li>LENGTH : 8 WEEKS</li>
      <li>FEE : SEE OFFER BELOW</li>
    </ul>
  </div>
  <div class="photo clinic-photo" role="img" aria-label="Kids in yellow bibs practising soccer drills"></div>
</section>
<div class="marker" style="top:2000px"></div>

<section class="section offer">
  <div class="photo offer-photo" role="img" aria-label="Young players with a coach on a training pitch"></div>
  <div class="offer-copy">
    <h2 class="heading">Special Offer</h2>
    <p class="offer-sub">Limited Places</p>
    <p>Book a full block of eight sessions and save on the regular weekly rate. Your child will train with our coaching team, receive a skills report at the end of the program and take home a training shirt. Places are limited to keep groups small and coaching personal, so register early to secure a spot.</p>
  </div>
</section>
<div class="marker" style="top:2420px;border-top-color:#2a3036"></div>

<section class="section pricing">
  <div class="price-box past">
    <div class="price-badge">$295</div>
    <div class="price-label"><div class="heading">For 8 Sessions</div><div class="who">Past JSA Participants</div></div>
  </div>
  <div class="price-box new">
    <div class="price-badge">$315</div>
    <div class="price-label"><div class="heading">For 8 Sessions</div><div class="who">New Participants</div></div>
  </div>
</section>

<section class="section cta">
  <h2 class="heading">Don't Miss Out!</h2>
  <p>Only 10 Spots Left - Register Your Interest Now</p>
</section>
<div class="marker" style="top:2800px"></div>

<section class="section register">
  <form class="register-form">
    <div class="field-label">First Name</div>
    <div class="field">First Name</div>
    <div class="field-label">Last Name</div>
    <div class="field">Last Name</div>
    <span class="btn-send">Send</span>
  </form>
  <div class="photo register-photo" role="img" aria-label="Junior soccer team in red kits lined up with balls"></div>
</section>

<footer class="section site-footer">
  <div class="footer-email">
    <svg width="16" height="12" viewBox="0 0 16 12"><rect x="0.5" y="0.5" width="15" height="11" fill="none" stroke="#fff"/><path d="M1 1l7 6 7-6" fill="none" stroke="#fff"/></svg>
    hello@juniorstride.com.au
  </div>
  <div class="footer-legal">© 2016 Junior Stride Athletics. All Rights Reserved. &nbsp;|&nbsp; Privacy Policy</div>
  <div class="follow">Follow Us On
    <div class="socials"><span></span><span></span><span></span><span></span></div>
  </div>
</footer>

</body>
</html>
```